Quillory Nest Business Card

I need a business card design. We are a collaborate online training company. Our colors are gray and green. Our website is QuilloryNest.com

I would like an area for a profile picture within the card

```html
<!DOCTYPE html>
<html lang="en">
<head>
<meta charset="utf-8">
<title>Quillory Nest Business Card</title>
<link rel="stylesheet" href="https://fonts.googleapis.com/css2?family=Lato:wght@400;700&family=PT+Sans+Narrow:wght@700&display=swap">
<style>
  :root {
    --green: #7dbb35;
    --ink: #141414;
    --white: #ffffff;
    --backdrop: #e6e6e4;
    --photo-a: #8a8580;
    --photo-b: #4a4542;
  }
  * { box-sizing: border-box; margin: 0; padding: 0; }
  html, body { width: 1200px; height: 955px; overflow: hidden; background: var(--backdrop); }
  .card { position: absolute; border-radius: 8px; overflow: hidden; }
  .brand {
    display: flex; align-items: center; gap: 12px;
    font-family: "PT Sans Narrow", sans-serif; font-weight: 700;
    letter-spacing: -1px; line-height: 1; white-space: nowrap;
  }
  .brand-dot { width: 44px; height: 44px; border-radius: 50%; flex: none; }

  /* front */
  .card-front { left: 338px; top: 158px; width: 534px; height: 306px; background: var(--white); }
  .card-front .brand { position: absolute; left: 34px; top: 50px; font-size: 50px; color: var(--ink); }
  .card-front .brand-dot { background: var(--green); }
  .profile-photo {
    position: absolute; left: 398px; top: 32px; width: 106px; height: 120px;
    border: 4px solid var(--green);
    background: linear-gradient(160deg, var(--photo-a), var(--photo-b));
  }
  .person-name { position: absolute; left: 31px; top: 154px; font: 700 21px "Lato", sans-serif; color: var(--green); }
  .person-role { position: absolute; left: 31px; top: 180px; font: 400 16px "Lato", sans-serif; color: var(--ink); }
  .role-rule { position: absolute; left: 98px; top: 192px; width: 406px; height: 1.5px; background: var(--green); }
  .contact-list { position: absolute; left: 31px; top: 222px; list-style: none; font: 400 14px "Lato", sans-serif; color: var(--ink); }
  .contact-list li { display: flex; align-items: center; gap: 6px; height: 18px; }
  .contact-list svg { width: 15px; height: 13px; fill: var(--green); }
  .address { position: absolute; right: 30px; top: 240px; text-align: right; font: 400 14px/18px "Lato", sans-serif; color: var(--ink); }
  .footer-band { position: absolute; left: 0; bottom: 0; width: 100%; height: 19px; background: var(--ink); }
  .footer-band::before {
    content: ""; position: absolute; left: 0; top: 0; width: 357px; height: 19px;
    background: var(--green); border-radius: 0 10px 10px 0; box-shadow: 1px 0 0 1px var(--white);
  }

  /* backs */
  .card-back { top: 531px; width: 533px; height: 304px; display: flex; align-items: center; justify-content: center; }
  .card-back .brand { font-size: 52px; }
  .card-back-green { left: 62px; background: var(--green); }
  .card-back-green .brand { color: var(--white); }
  .card-back-green .brand-dot { background: var(--white); }
  .card-back-dark { left: 630px; background: #000; }
  .card-back-dark .brand { color: var(--green); }
  .card-back-dark .brand-dot { background: var(--green); }
</style>
</head>
<body>
  <section class="card card-front">
    <div class="brand"><span class="brand-dot"></span>Quillory Nest</div>
    <div class="profile-photo" role="img" aria-label="Profile photo of the founder"></div>
    <h1 class="person-name">Dorian Pell</h1>
    <p class="person-role">Founder</p>
    <div class="role-rule"></div>
    <ul class="contact-list">
      <li><svg viewBox="0 0 16 14"><path d="M1 5c0-3 14-3 14 0v1h-4V4H5v2H1z M4 7h8l2 6H2z"/></svg>(302) 555-0147</li>
      <li><svg viewBox="0 0 16 14"><path d="M1 2h14v10H1z" fill="none" stroke="#7dbb35" stroke-width="1.5"/><path d="M1 2l7 6 7-6" fill="none" stroke="#7dbb35" stroke-width="1.5"/></svg>dorian@quillorynest.com</li>
      <li><svg viewBox="0 0 16 14"><g fill="none" stroke="#7dbb35" stroke-width="1.3"><circle cx="8" cy="7" r="6"/><ellipse cx="8" cy="7" rx="2.6" ry="6"/><path d="M2 7h12M3 4h10M3 10h10"/></g></svg>www.quillorynest.com</li>
    </ul>
    <p class="address">4810 W Alder Row Blvd<br>Suite 11 Fenwick, Arizona 85299</p>
    <div class="footer-band"></div>
  </section>

  <section class="card card-back card-back-green">
    <div class="brand"><span class="brand-dot"></span>Quillory Nest</div>
  </section>

  <section class="card card-back card-back-dark">
    <div class="brand"><span class="brand-dot"></span>Quillory Nest</div>
  </section>
</body>
</html>
```